Ardent Tech Business Card - Clean, Simple

Need a simple, clean standard sized business card for an IT consulting business using existing logo and company colours. Background should be mainly white. Feel free to be creative but clean, simple, quiet design is preferred. Font is specified in logo but any sans serif fonts work.

Contact Information for card is as follows (doesn't need to be in this exact order):

Martin Calloway
Owner
martin@ardenttech.ca
555-555-0142
www.ardenttech.ca

Target Market(s)

Small to medium sized business.

Industry/Entity Type

IT Consulting

Contact Information for Business Card

Logo and contact info.

Font styles to use
Sans Serif

Colors
EE7325
F08F49
F5BC92
FAE3D3
FDF4ED

Requirements
Must have
• All white or mostly white background.

```html
<!DOCTYPE html>
<html lang="en">
<head>
<meta charset="utf-8">
<title>Ardent Tech – Business Card</title>
<link href="https://fonts.googleapis.com/css2?family=Poppins:wght@400;500;600&display=swap" rel="stylesheet">
<style>
  :root {
    --orange: #EE7325;
    --orange-soft: #F08F49;
    --charcoal: #313131;
    --ink: #2f2f2f;
    --white: #ffffff;
    --page: #eeeeee;
  }
  * { margin: 0; padding: 0; box-sizing: border-box; }
  html, body {
    width: 1200px; height: 900px; overflow: hidden;
    background: var(--page);
    font-family: "Poppins", sans-serif;
  }
  .business-card {
    position: absolute;
    left: 100px; top: 141px;
    width: 1000px; height: 618px;
    background: var(--white);
    overflow: hidden;
    box-shadow: 0 6px 24px rgba(0,0,0,0.12);
  }
  .card-shapes { position: absolute; inset: 0; width: 100%; height: 100%; }
  .brand-mark {
    position: absolute;
    left: 166px; top: 62px;
    width: 150px; height: 150px;
    border-radius: 50%;
    background: var(--orange);
  }
  .brand-name {
    position: absolute;
    left: 20px; width: 446px; top: 232px;
    text-align: center;
    font-size: 60px; font-weight: 600; line-height: 72px;
    letter-spacing: -0.5px;
    color: var(--ink);
    white-space: nowrap;
  }
  .holder { position: absolute; left: 566px; top: 168px; }
  .holder-name {
    font-size: 41px; font-weight: 500;
    color: var(--orange); line-height: 48px;
    white-space: nowrap;
  }
  .holder-role {
    font-size: 27px; font-weight: 400;
    color: var(--white); line-height: 32px;
    margin-left: 5px;
  }
  .contact-list { position: absolute; left: 574px; top: 320px; list-style: none; }
  .contact-item {
    display: flex; align-items: center;
    height: 37px;
    font-size: 31px; color: var(--white);
    white-space: nowrap;
  }
  .contact-icon { width: 26px; height: 26px; margin-right: 16px; flex: none; }
</style>
</head>
<body>
  <div class="business-card">
    <svg class="card-shapes" viewBox="0 0 1000 618" aria-hidden="true">
      <path class="accent-curve" fill="#EE7325"
        d="M440,0 C495,70 512,160 497,250 C484,330 445,390 428,470 C425,400 455,340 475,260 C495,180 500,80 481,0 Z"/>
      <path class="info-panel" fill="#313131"
        d="M481,0 C500,80 495,180 475,260 C455,340 425,400 427,470 C428,530 440,580 458,618 L1000,618 L1000,0 Z"/>
    </svg>

    <div class="brand-mark"></div>
    <div class="brand-name">Ardent Tech</div>

    <div class="holder">
      <div class="holder-name">Martin Calloway</div>
      <div class="holder-role">Owner</div>
    </div>

    <ul class="contact-list">
      <li class="contact-item">
        <svg class="contact-icon" viewBox="0 0 24 24" fill="none" stroke="#EE7325" stroke-width="2" stroke-linejoin="round">
          <path d="M5 3h4l2 5-2.5 1.5a11 11 0 0 0 6 6L16 13l5 2v4a2 2 0 0 1-2 2A17 17 0 0 1 3 5a2 2 0 0 1 2-2z"/>
          <path d="M15 3a6 6 0 0 1 6 6M15 7a2 2 0 0 1 2 2" stroke-linecap="round"/>
        </svg>
        555-555-0142
      </li>
      <li class="contact-item">
        <svg class="contact-icon" viewBox="0 0 24 24">
          <rect x="1" y="5" width="22" height="15" fill="#EE7325"/>
          <path d="M1 5l11 8 11-8" fill="none" stroke="#313131" stroke-width="1.6"/>
        </svg>
        martin@ardenttech.ca
      </li>
      <li class="contact-item">
        <svg class="contact-icon" viewBox="0 0 24 24" fill="none" stroke="#EE7325" stroke-width="1.8">
          <circle cx="12" cy="12" r="10"/>
          <ellipse cx="12" cy="12" rx="4.5" ry="10"/>
          <path d="M2 12h20M4 7h16M4 17h16"/>
        </svg>
        www.ardenttech.ca
      </li>
    </ul>
  </div>
</body>
</html>
```